Business Card/Design Project for Personal Injury Lawyer

Personal Injury Attorney. I represent people who have been injured in accidents and are making money damage claims against the negligent party. As a personal injury attorney, I am a counselor, advisor, and legal representative to my clients. Clients want someone who is aggresssive yet professional.

More information about what I do an be found at www.dravolinlaw.com

Target Market(s)

General public.

Industry/Entity Type

Legal

Contact Information for Business Card

Need a new logo/brand image for b-cards, website, and letterhead/envelops. Looking for something original (no scales of justice or courthouse columns), yet classy and professional.

Here's what I'm thinking (but I'm always open to other ideas):

On the front, I would like my name (Corwin T. Dravolin), and underneath the words "Personal Injury Attorney." The background could be black, for example, and the lettering could be white or foil. I'm open to differnt colors, or even two colors. My name on the front side should pop.

And then on the back would be all my contact info, and maybe a logo or a slogan.

Here are two slogans I've come up with so far: 1. Demand More. 2. Real Results for the Seriously Hurt.

Requirements
Must have
• Something that identifys me as a personal injury attorney, such as the words Personal Injury Attorney (or Lawyer, or Law Firm, etc.).
Nice to have
• A style/image that can be used nicely on my website and on letterhead.
Should not have
• Tired, commonly used logos or symbols, such a scales of justice or courthouse columns.

```html
<!DOCTYPE html>
<html lang="en">
<head>
<meta charset="utf-8">
<title>Dravolin Law – Business Card</title>
<link href="https://fonts.googleapis.com/css2?family=Open+Sans:wght@400;600&display=swap" rel="stylesheet">
<style>
  :root {
    --page: #ffffff;
    --card: #000000;
    --band: #4a4a4a;
    --gold: #f2bd4e;
    --mark-grey: #3c3c3c;
    --grey-text: #8a8a8a;
    --light-text: #a8a8a8;
    --band-text: #1c1c1c;
    --pill: #474747;
    --pill-text: #cfcfcf;
    --shadow: rgba(0,0,0,0.35);
  }
  * { margin: 0; padding: 0; box-sizing: border-box; }
  html, body { width: 1200px; height: 892px; overflow: hidden; background: var(--page); }
  body { position: relative; font-family: "Open Sans", Arial, sans-serif; }

  .card {
    position: absolute;
    left: 336px;
    width: 573px;
    height: 322px;
    background: var(--card);
    box-shadow: 8px 10px 14px var(--shadow);
  }
  .card--front { top: 86px; }
  .card--back { top: 497px; }

  /* front */
  .brand-mark {
    position: absolute; top: 76px; left: 0; width: 100%;
    text-align: center; color: var(--mark-grey);
    font-weight: 600; font-size: 22px; line-height: 28px; letter-spacing: 1px;
  }
  .attorney-name {
    position: absolute; top: 158px; left: 0; width: 100%;
    text-align: center; color: var(--gold);
    font-weight: 600; font-size: 30px; line-height: 40px;
  }
  .attorney-title {
    position: absolute; top: 200px; left: 0; width: 100%;
    text-align: center; color: var(--grey-text);
    font-weight: 400; font-size: 16px; line-height: 22px;
  }
  .slogan-pill {
    position: absolute; top: 266px; left: 60px; width: 394px; height: 25px;
    background: var(--pill); border-radius: 4px;
    color: var(--pill-text); font-size: 14px; line-height: 25px; text-align: center;
  }

  /* back */
  .side-band {
    position: absolute; top: 0; left: 0; width: 108px; height: 100%;
    background: var(--band);
  }
  .side-band__tagline {
    position: absolute; left: 13px; bottom: 36px;
    writing-mode: vertical-rl; transform: rotate(180deg);
    white-space: nowrap; color: var(--band-text);
    font-size: 15px; line-height: 20px;
  }
  .side-band__brand {
    position: absolute; top: 54px; left: 46px;
    color: var(--gold); font-weight: 600; font-size: 12px; line-height: 16px;
  }
  .firm-name {
    position: absolute; top: 59px; left: 130px;
    color: var(--light-text); font-weight: 400; font-size: 31px; line-height: 34px;
  }
  .contact-list {
    position: absolute; top: 143px; left: 130px; list-style: none;
  }
  .contact-list li {
    display: flex; align-items: center; height: 22.5px;
    color: var(--grey-text); font-size: 14.5px;
  }
  .contact-list svg { width: 14px; height: 14px; margin-right: 10px; fill: var(--grey-text); }
  .motto-pill {
    position: absolute; top: 259px; left: 129px; width: 142px; height: 25px;
    background: var(--pill); border-radius: 4px;
    color: var(--pill-text); font-size: 15.5px; line-height: 25px; text-align: center;
  }
</style>
</head>
<body>

<section class="card card--front">
  <div class="brand-mark">Dravolin</div>
  <h1 class="attorney-name">Corwin T. Dravolin</h1>
  <p class="attorney-title">Personal Injury Attorney</p>
  <div class="slogan-pill">Real Results for the Seriously Hurt</div>
</section>

<section class="card card--back">
  <div class="side-band">
    <p class="side-band__tagline">Free Case Review Open 24/7</p>
    <span class="side-band__brand">Dravolin</span>
  </div>
  <h2 class="firm-name">Dravolin Law</h2>
  <ul class="contact-list">
    <li><svg viewBox="0 0 16 16"><path d="M3 2h3l1.5 3.5-2 1.2a8 8 0 0 0 3.8 3.8l1.2-2L14 10v3a1 1 0 0 1-1 1A11 11 0 0 1 2 3a1 1 0 0 1 1-1z"/></svg>305.555.0148</li>
    <li><svg viewBox="0 0 16 16"><g fill="none" stroke="#8a8a8a" stroke-width="1.3"><circle cx="8" cy="8" r="6.3"/><ellipse cx="8" cy="8" rx="2.8" ry="6.3"/><line x1="1.7" y1="8" x2="14.3" y2="8"/></g></svg>www.dravolinlaw.com</li>
    <li><svg viewBox="0 0 16 16"><rect x="1.5" y="3.5" width="13" height="9"/></svg>Corwin@dravolinlaw.com</li>
    <li><svg viewBox="0 0 16 16"><path d="M8 1a5 5 0 0 1 5 5c0 3.6-5 9-5 9S3 9.6 3 6a5 5 0 0 1 5-5zm0 3a2 2 0 1 0 0 4 2 2 0 0 0 0-4z"/></svg>2240 Harbor Ave., Suite 410, Coral Bay, FL 33904</li>
  </ul>
  <div class="motto-pill">Demand More</div>
</section>

</body>
</html>
```